Physcial Activity & Parkinson's Disease Severity

We are very happy with the with the infographic below (on diet and PD progression). Now, we need a new infographic on the relationship between physical activity and PD progression.

Target Market(s)

Individuals with parkinonsonism (35-100 y), both genders, as well as their physicians, family members, support group leaders, etc.

Industry/Entity Type

Medicine

Requirements
Must have
• The same information as is listed in the top left corner of the previous infographic on Diet. (For more information: www.brightstepwellnessforall.com, For study info: www.TRVStudyQN.Holmecrest.edu), 2020, RT Vandorne, etc.
Nice to have
• It should fit in nicely with the other ones from a design standpoint.

```html
<!DOCTYPE html>
<html lang="en">
<head>
<meta charset="utf-8">
<title>Physical Activity and Parkinson's Disease Severity — 2020</title>
<link rel="stylesheet" href="https://fonts.googleapis.com/css2?family=Roboto+Condensed:ital,wght@0,400;0,500;0,700;1,500&family=Montserrat:wght@400;500;600&display=swap">
<style>
  :root{
    --page:#e4e3e2;
    --frame:#dfeef8;
    --paper:#ffffff;
    --purple:#a07bbb;
    --ink:#111111;
    --poor:#bd1e2e;
    --fair:#1a7abf;
    --good:#5e2b8e;
    --excellent:#9bc15a;
    --line-blue:#3b8fd6;
    --line-purple:#a07bbb;
  }
  *{margin:0;padding:0;box-sizing:border-box}
  html,body{width:1050px;height:1200px;overflow:hidden;background:var(--page)}
  body{position:relative;font-family:"Roboto Condensed",Arial,sans-serif;color:var(--ink)}
  .panel{position:absolute;width:461px;height:346px;background:var(--frame);box-shadow:0 12px 14px -6px rgba(0,0,0,.35)}
  .panel svg{display:block;width:461px;height:346px}
  .panel--title{left:41px;top:42px}
  .panel--quality{left:545px;top:42px}
  .panel--activities{left:41px;top:420px}
  .panel--frequency{left:545px;top:420px}
  .panel--weight{left:295px;top:799px}
  .cond{font-family:"Roboto Condensed",Arial,sans-serif}
  .mont{font-family:"Montserrat",Arial,sans-serif}
</style>
</head>
<body>

<section class="panel panel--title" aria-label="Title and study details">
  <svg viewBox="0 0 461 346">
    <rect x="11" y="123" width="439" height="212" fill="var(--paper)"/>
    <text class="cond" x="230.5" y="43" text-anchor="middle" font-size="40" font-weight="700" fill="var(--purple)" textLength="405" lengthAdjust="spacingAndGlyphs">PHYSCIAL ACTIVITY AND</text>
    <text class="cond" x="230.5" y="74" text-anchor="middle" font-size="31" font-weight="700" fill="var(--purple)" textLength="405" lengthAdjust="spacingAndGlyphs">PARKINSON'S DISEASE SEVERITY</text>
    <rect x="169" y="86" width="123" height="27" rx="13.5" fill="var(--ink)" stroke="var(--paper)" stroke-width="1.5"/>
    <text class="cond" x="230.5" y="107" text-anchor="middle" font-size="22" font-weight="700" fill="#fff">2020</text>
    <text class="cond" x="230.5" y="160" text-anchor="middle" font-size="18" font-style="italic" font-weight="500">RT Vandorne et al.</text>
    <circle cx="218" cy="176" r="3.6" fill="none" stroke="var(--purple)" stroke-width="1"/>
    <circle cx="229.5" cy="176" r="3.8" fill="var(--purple)"/>
    <circle cx="241" cy="176" r="3.6" fill="none" stroke="var(--purple)" stroke-width="1"/>
    <text class="cond" x="230.5" y="213" text-anchor="middle" font-size="18">For Study Details</text>
    <rect x="89" y="221" width="282" height="23" rx="11.5" fill="var(--purple)"/>
    <text class="cond" x="230.5" y="238" text-anchor="middle" font-size="15" fill="#fff">www.brightstepwellnessforall.com</text>
    <text class="cond" x="230.5" y="282" text-anchor="middle" font-size="18">To participate in the study</text>
    <rect x="89" y="292" width="282" height="23" rx="11.5" fill="var(--purple)"/>
    <text class="cond" x="230.5" y="309" text-anchor="middle" font-size="15" fill="#fff">www.TRVStudyQN.Holmecrest.edu</text>
  </svg>
</section>

<section class="panel panel--quality" aria-label="Correlation between quality of life and PRO-PD score">
  <svg viewBox="0 0 461 346" class="mont">
    <rect x="11" y="11" width="439" height="324" fill="var(--paper)"/>
    <text x="255" y="40" text-anchor="middle" font-size="12" font-weight="500">Correlation Between</text>
    <rect x="158" y="47" width="191" height="19" rx="9.5" fill="var(--ink)"/>
    <text x="253.5" y="60.5" text-anchor="middle" font-size="10.5" font-weight="500" fill="#fff">Quality of life and PRO-PD Score</text>

    <rect x="91" y="83" width="247" height="76" fill="var(--poor)"/>
    <rect x="91" y="159" width="247" height="35" fill="var(--fair)"/>
    <rect x="91" y="194" width="247" height="38" fill="var(--good)"/>
    <rect x="91" y="232" width="247" height="36" fill="var(--excellent)"/>
    <rect x="356" y="83" width="62" height="76" fill="var(--poor)"/>
    <rect x="356" y="159" width="62" height="35" fill="var(--fair)"/>
    <rect x="356" y="194" width="62" height="38" fill="var(--good)"/>
    <rect x="356" y="232" width="62" height="36" fill="var(--excellent)"/>
    <g font-size="8" fill="#fff" text-anchor="middle">
      <text x="387" y="124">Poor</text>
      <text x="387" y="179">Fair</text>
      <text x="387" y="216">Good</text>
      <text x="387" y="253">Excellent</text>
    </g>

    <g font-size="7" font-weight="600" text-anchor="end">
      <text x="84" y="86">2500</text>
      <text x="84" y="123">2000</text>
      <text x="84" y="160">1500</text>
      <text x="84" y="197">1000</text>
      <text x="84" y="234">500</text>
      <text x="84" y="271">0</text>
    </g>
    <g font-size="7" font-weight="600" text-anchor="middle">
      <text x="138" y="279">5</text><text x="183" y="279">10</text><text x="231" y="279">15</text>
      <text x="279" y="279">20</text><text x="326" y="279">25</text><text x="370" y="279">30</text><text x="417" y="279">35</text>
    </g>

    <polyline points="91,225 338,158" fill="none" stroke="#fff" stroke-width="1"/>
    <polyline points="356,153 380,146" fill="none" stroke="#fff" stroke-width="1"/>
    <g fill="var(--ink)" stroke="#fff" stroke-width="1">
      <circle cx="138" cy="213" r="3.2"/><circle cx="185" cy="200" r="3.2"/><circle cx="232" cy="187" r="3.2"/>
      <circle cx="278" cy="174" r="3.2"/><circle cx="324" cy="161" r="3.2"/><circle cx="371" cy="148" r="3.2"/>
    </g>

    <rect x="37" y="124" width="19" height="103" rx="9.5" fill="var(--purple)"/>
    <text x="0" y="0" transform="translate(50.5 175.5) rotate(-90)" text-anchor="middle" font-size="10" font-weight="500" fill="#fff">PRO-PD Score</text>
    <text x="0" y="0" transform="translate(350 174) rotate(-90)" text-anchor="middle" font-size="11" font-weight="500">Quality of life</text>

    <line x1="118" y1="304" x2="389" y2="304" stroke="var(--ink)" stroke-width="1"/>
    <path d="M116 304 l6 -3 v6 z M391 304 l-6 -3 v6 z" fill="var(--ink)"/>
    <rect x="180" y="295" width="147" height="18" rx="9" fill="var(--ink)"/>
    <text x="253.5" y="307.5" text-anchor="middle" font-size="10.5" font-weight="500" fill="#fff">Years Since Diagnosis</text>
  </svg>
</section>

<section class="panel panel--activities" aria-label="Activities and PRO-PD improvement">
  <svg viewBox="0 0 461 346" class="mont">
    <rect x="11" y="11" width="439" height="324" fill="var(--paper)"/>
    <rect x="159" y="32" width="190" height="18" rx="9" fill="var(--ink)"/>
    <text x="254" y="45" text-anchor="middle" font-size="10.5" font-weight="500" fill="#fff">STATISTICALLY SIGNIFICANT</text>

    <g font-size="7.5" font-weight="500" text-anchor="end">
      <text x="49" y="64">300</text><text x="49" y="92">250</text><text x="49" y="119">200</text>
      <text x="49" y="147">150</text><text x="49" y="175">100</text><text x="49" y="203">50</text>
      <text x="49" y="230">0</text><text x="49" y="258">-50</text>
    </g>
    <line x1="59" y1="56" x2="59" y2="255" stroke="var(--ink)" stroke-width="0.8"/>
    <path d="M59 52 l-2.5 6 h5 z" fill="var(--ink)"/>
    <line x1="59" y1="255" x2="371" y2="255" stroke="var(--ink)" stroke-width="0.8"/>
    <path d="M374 255 l-6 -2.5 v5 z" fill="var(--ink)"/>
    <line x1="53" y1="227.4" x2="428" y2="227.4" stroke="var(--ink)" stroke-width="0.6" stroke-dasharray="2.5 2"/>

    <g fill="var(--purple)">
      <rect x="67" y="111.9" width="16" height="115.5"/>
      <rect x="105" y="166.4" width="16" height="61"/>
      <rect x="143" y="178.7" width="16" height="48.7"/>
      <rect x="180" y="182.2" width="16" height="45.2"/>
      <rect x="218" y="186.3" width="16" height="41.1"/>
      <rect x="255" y="202.2" width="16" height="25.2"/>
      <rect x="293" y="202.2" width="16" height="25.2"/>
      <rect x="331" y="209.8" width="16" height="17.6"/>
      <rect x="368" y="222.1" width="16" height="5.3"/>
      <rect x="406" y="225" width="16" height="2.4"/>
    </g>
    <g stroke="var(--ink)" stroke-width="0.6">
      <line x1="75" y1="91.4" x2="75" y2="111.9"/><line x1="113" y1="153.5" x2="113" y2="166.4"/>
      <line x1="151" y1="162.9" x2="151" y2="178.7"/><line x1="188" y1="162.3" x2="188" y2="182.2"/>
      <line x1="226" y1="171.7" x2="226" y2="186.3"/><line x1="263" y1="188.1" x2="263" y2="202.2"/>
      <line x1="301" y1="181.7" x2="301" y2="202.2"/><line x1="339" y1="189.9" x2="339" y2="229.7"/>
      <line x1="376" y1="197.5" x2="376" y2="245.5"/><line x1="414" y1="207.5" x2="414" y2="245"/>
    </g>
    <g fill="var(--ink)">
      <circle cx="75" cy="91.4" r="1"/><circle cx="113" cy="153.5" r="1"/><circle cx="151" cy="162.9" r="1"/>
      <circle cx="188" cy="162.3" r="1"/><circle cx="226" cy="171.7" r="1"/><circle cx="263" cy="188.1" r="1"/>
      <circle cx="301" cy="181.7" r="1"/><circle cx="339" cy="189.9" r="1"/><circle cx="339" cy="229.7" r="1"/>
      <circle cx="376" cy="197.5" r="1"/><circle cx="376" cy="245.5" r="1"/><circle cx="414" cy="207.5" r="1"/><circle cx="414" cy="245" r="1"/>
    </g>
    <g font-size="5.5" text-anchor="middle" fill="var(--ink)">
      <text x="75" y="86">209</text><text x="113" y="149">111</text><text x="151" y="159.5">89</text>
      <text x="188" y="159.5">83</text><text x="226" y="166">75</text><text x="263" y="183.5">46</text>
      <text x="301" y="177.5">46</text><text x="339" y="186">33</text><text x="376" y="194">10</text><text x="414" y="203.5">2</text>
    </g>
    <g font-size="6.5" text-anchor="middle" fill="var(--purple)">
      <text x="75" y="79">★</text><text x="113" y="142">★</text><text x="151" y="153">★</text>
      <text x="188" y="153">★</text><text x="226" y="159.5">★</text>
    </g>
    <g font-size="5.6" text-anchor="middle">
      <text x="75" y="267">9.9%</text><text x="75" y="275">Running</text>
      <text x="113" y="267">46.2%</text><text x="113" y="275">Other</text>
      <text x="151" y="267">22.5%</text><text x="151" y="275">Yoga</text>
      <text x="188" y="267">11.9%</text><text x="188" y="275">Hiking</text>
      <text x="226" y="267">125.0%</text><text x="226" y="275">Biking</text>
      <text x="263" y="267">73.5%</text><text x="263" y="275">Walking</text>
      <text x="301" y="267">10.0%</text><text x="301" y="275">Tai Chi</text>
      <text x="339" y="267">11.4%</text><text x="339" y="275">Dance</text>
      <text x="376" y="267">6.8%</text><text x="376" y="275">Bold</text><text x="376" y="283">Stride Boxing</text>
      <text x="414" y="267">10.6%</text><text x="414" y="275">Swimming</text>
    </g>

    <line x1="113" y1="305" x2="384" y2="305" stroke="var(--ink)" stroke-width="1"/>
    <path d="M111 305 l6 -3 v6 z M386 305 l-6 -3 v6 z" fill="var(--ink)"/>
    <rect x="172" y="296" width="148" height="18" rx="9" fill="var(--ink)"/>
    <text x="246" y="308.5" text-anchor="middle" font-size="10.5" font-weight="500" fill="#fff">% reporting participation</text>
  </svg>
</section>

<section class="panel panel--frequency" aria-label="Exercise frequency and mean PRO-PD">
  <svg viewBox="0 0 461 346" class="mont">
    <rect x="11" y="11" width="439" height="324" fill="var(--paper)"/>
    <rect x="20" y="36" width="60" height="11" rx="5.5" fill="var(--purple)"/>
    <text x="50" y="44.3" text-anchor="middle" font-size="7" fill="#fff">Mean PRO-PD</text>
    <rect x="86" y="36" width="70" height="11" rx="5.5" fill="var(--purple)"/>
    <text x="121" y="44.3" text-anchor="middle" font-size="7" fill="#fff">% of Participants</text>

    <g font-size="7" text-anchor="middle">
      <text x="51" y="70">664</text><text x="51" y="101">676</text><text x="51" y="132">715</text><text x="51" y="162.5">762</text>
      <text x="51" y="193.5">815</text><text x="51" y="224.5">1032</text><text x="51" y="255">1015</text><text x="51" y="286">1029</text>
    </g>
    <g font-size="7" text-anchor="middle">
      <text x="121" y="70">20%</text><text x="121" y="101">15%</text><text x="121" y="132">17%</text><text x="121" y="162.5">15%</text>
      <text x="121" y="193.5">13%</text><text x="121" y="224.5">9%</text><text x="121" y="255">4%</text><text x="121" y="286">6%</text>
    </g>
    <g font-size="4.6" text-anchor="end">
      <text x="207" y="69">Exercise 30+ min/d, 7 days/wk</text><text x="207" y="100">Exercise 30+ min/d, 6 days/wk</text>
      <text x="207" y="131">Exercise 30+ min/d, 5 days/wk</text><text x="207" y="161.5">Exercise 30+ min/d, 4 days/wk</text>
      <text x="207" y="192.5">Exercise 30+ min/d, 3 days/wk</text><text x="207" y="223.5">Exercise 30+ min/d, 2 days/wk</text>
      <text x="207" y="254">Exercise 30+ min/d, 1 days/wk</text><text x="207" y="285">Exercise 30+ min/d, 0 days/wk</text>
    </g>
    <g font-size="4.8" text-anchor="middle">
      <text x="227" y="69">-301</text><text x="227" y="100">-292</text><text x="227" y="131">-237</text><text x="227" y="161.5">-229</text>
      <text x="227" y="192.5">-192</text><text x="227" y="223.5">-20</text><text x="227" y="254">-59</text>
    </g>

    <line x1="216" y1="51" x2="216" y2="298" stroke="var(--ink)" stroke-width="0.8"/>
    <path d="M216 47 l-2.5 6 h5 z" fill="var(--ink)"/>
    <line x1="216" y1="298" x2="425" y2="298" stroke="var(--ink)" stroke-width="0.8"/>
    <path d="M429 298 l-6 -2.5 v5 z" fill="var(--ink)"/>
    <g font-size="4.6" text-anchor="middle">
      <text x="217" y="306">-400</text><text x="238" y="306">-350</text><text x="260" y="306">-300</text>
      <text x="281" y="306">-250</text><text x="303" y="306">-200</text><text x="324" y="306">-150</text>
      <text x="344" y="306">-100</text><text x="364" y="306">-50</text><text x="382" y="306">-0</text>
      <text x="405" y="306">50</text><text x="425" y="306">100</text>
    </g>

    <g stroke="var(--ink)" stroke-width="0.5">
      <line x1="236" y1="67" x2="254" y2="67"/><line x1="240" y1="98" x2="258" y2="98"/>
      <line x1="262" y1="129" x2="283" y2="129"/><line x1="265" y1="159.6" x2="287" y2="159.6"/>
      <line x1="282" y1="190.6" x2="302" y2="190.6"/><line x1="349" y1="221.6" x2="400" y2="221.6"/>
      <line x1="328" y1="252.2" x2="387" y2="252.2"/>
    </g>
    <g fill="var(--ink)">
      <circle cx="236" cy="67" r="0.9"/><circle cx="240" cy="98" r="0.9"/><circle cx="262" cy="129" r="0.9"/>
      <circle cx="265" cy="159.6" r="0.9"/><circle cx="282" cy="190.6" r="0.9"/><circle cx="349" cy="221.6" r="0.9"/>
      <circle cx="400" cy="221.6" r="0.9"/><circle cx="328" cy="252.2" r="0.9"/><circle cx="387" cy="252.2" r="0.9"/>
    </g>
    <g fill="var(--purple)">
      <rect x="254" y="60.5" width="129" height="13"/><rect x="258" y="91.5" width="125" height="13"/>
      <rect x="283" y="122.5" width="100" height="13"/><rect x="287" y="153" width="96" height="13"/>
      <rect x="302" y="184" width="81" height="13"/><rect x="374" y="215" width="9" height="13"/>
      <rect x="357" y="245.7" width="26" height="13"/>
    </g>

    <rect x="408" y="197" width="9" height="81" rx="4.5" fill="var(--purple)"/>
    <text x="0" y="0" transform="translate(414.3 237.5) rotate(-90)" text-anchor="middle" font-size="4.6" fill="#fff">Not Statistically Significant</text>
  </svg>
</section>

<section class="panel panel--weight" aria-label="Overweight individuals reported greater symptom severity">
  <svg viewBox="0 0 461 346" class="mont">
    <rect x="11" y="11" width="439" height="324" fill="var(--paper)"/>
    <text x="230" y="40" text-anchor="middle" font-size="12" font-weight="500">Overweight Individuals Reported</text>
    <rect x="148" y="47" width="162" height="18" rx="9" fill="var(--purple)"/>
    <text x="229" y="59.5" text-anchor="middle" font-size="10.5" font-weight="500" fill="#fff">Greater Symptom Severity</text>

    <line x1="144" y1="83" x2="161" y2="83" stroke="var(--line-blue)" stroke-width="1"/>
    <circle cx="152.5" cy="83" r="2.4" fill="#fff" stroke="var(--line-blue)" stroke-width="1"/>
    <text x="167" y="85.5" font-size="7" font-weight="500">OVERWEIGHT</text>
    <line x1="229" y1="83" x2="247" y2="83" stroke="var(--line-purple)" stroke-width="1"/>
    <circle cx="238" cy="83" r="2.4" fill="#fff" stroke="var(--line-purple)" stroke-width="1"/>
    <text x="253" y="85.5" font-size="7" font-weight="500">NOT OVERWEIGHT</text>

    <g font-size="7.5" font-weight="500" text-anchor="end">
      <text x="81" y="83">300</text><text x="81" y="110.5">250</text><text x="81" y="138">200</text>
      <text x="81" y="166">150</text><text x="81" y="193.5">100</text><text x="81" y="221">50</text>
      <text x="81" y="249">0</text><text x="81" y="276.5">-50</text>
    </g>
    <line x1="91" y1="75" x2="91" y2="275" stroke="var(--ink)" stroke-width="0.8"/>
    <path d="M91 71 l-2.5 6 h5 z" fill="var(--ink)"/>
    <line x1="91" y1="275" x2="388" y2="275" stroke="var(--ink)" stroke-width="0.8"/>
    <path d="M392 275 l-6 -2.5 v5 z" fill="var(--ink)"/>
    <g font-size="6.5" font-weight="500" text-anchor="middle">
      <text x="104" y="288">0</text><text x="130" y="288">1</text><text x="157" y="288">2</text><text x="184" y="288">3</text>
      <text x="210" y="288">4</text><text x="237" y="288">5</text><text x="265" y="288">6</text><text x="291" y="288">7</text>
      <text x="318" y="288">8</text><text x="345" y="288">9</text><text x="373" y="288">10</text>
    </g>

    <polyline points="104,201.6 130,202.8 157,198.1 184,187.5 210,195.7 237,174.6 265,164.1 291,157.6 318,165.3 345,155.3 373,140.6" fill="none" stroke="var(--line-purple)" stroke-width="1.1"/>
    <g fill="#fff" stroke="var(--line-purple)" stroke-width="1.1">
      <circle cx="104" cy="201.6" r="2.5"/><circle cx="130" cy="202.8" r="2.5"/><circle cx="157" cy="198.1" r="2.5"/>
      <circle cx="184" cy="187.5" r="2.5"/><circle cx="210" cy="195.7" r="2.5"/><circle cx="237" cy="174.6" r="2.5"/>
      <circle cx="265" cy="164.1" r="2.5"/><circle cx="291" cy="157.6" r="2.5"/><circle cx="318" cy="165.3" r="2.5"/>
      <circle cx="345" cy="155.3" r="2.5"/><circle cx="373" cy="140.6" r="2.5"/>
    </g>
    <polyline points="104,180.5 130,171.1 157,177 184,179.9 210,165.3 237,167.1 265,142.5 291,165.3 318,138.9 345,127.2 373,114.9" fill="none" stroke="var(--line-blue)" stroke-width="1.1"/>
    <g fill="#fff" stroke="var(--line-blue)" stroke-width="1.1">
      <circle cx="104" cy="180.5" r="2.5"/><circle cx="130" cy="171.1" r="2.5"/><circle cx="157" cy="177" r="2.5"/>
      <circle cx="184" cy="179.9" r="2.5"/><circle cx="210" cy="165.3" r="2.5"/><circle cx="237" cy="167.1" r="2.5"/>
      <circle cx="265" cy="142.5" r="2.5"/><circle cx="291" cy="157.6" r="2.5" stroke="none" fill="none"/><circle cx="291" cy="165.3" r="2.5"/><circle cx="318" cy="138.9" r="2.5"/>
      <circle cx="345" cy="127.2" r="2.5"/><circle cx="373" cy="114.9" r="2.5"/>
    </g>
    <g font-size="4.8" text-anchor="middle">
      <text x="102" y="174">727</text><text x="128" y="165">803</text><text x="156" y="171">759</text>
      <text x="184" y="174">735</text><text x="208" y="159.5">841</text><text x="235" y="161.5">825</text>
      <text x="263" y="136.5">1009</text><text x="289" y="151">846</text><text x="316" y="133">1021</text>
      <text x="343" y="121" fill="#777">1107</text><text x="373" y="109">1194</text>
    </g>
    <g font-size="4.8" text-anchor="middle">
      <text x="104" y="210.5">582</text><text x="130" y="211.5">569</text><text x="158" y="207">598</text>
      <text x="186" y="196.5">685</text><text x="212" y="204.5">618</text><text x="240" y="183.5">771</text>
      <text x="266" y="173">845</text><text x="293" y="174">899</text><text x="320" y="173.5">845</text>
      <text x="346" y="164">898</text><text x="377" y="149">1001</text>
    </g>

    <rect x="38" y="133" width="19" height="86" rx="9.5" fill="var(--purple)"/>
    <text x="0" y="0" transform="translate(51.5 176) rotate(-90)" text-anchor="middle" font-size="10" font-weight="500" fill="#fff">PRO - PD</text>

    <line x1="110" y1="308" x2="364" y2="308" stroke="var(--ink)" stroke-width="1"/>
    <path d="M108 308 l6 -3 v6 z M366 308 l-6 -3 v6 z" fill="var(--ink)"/>
    <rect x="172" y="299" width="131" height="17" rx="8.5" fill="var(--ink)"/>
    <text x="237.5" y="311" text-anchor="middle" font-size="10.5" font-weight="500" fill="#fff">Years Since Diagnosis</text>
  </svg>
</section>

</body>
</html>
```